FREE Network Assessment image for landing page

This graphic will be on a landing page and on the left will be Text and a download button that we change and control. The graphic for this project will be to the right.
I will add an example of the landing page area so that it makes more sense.

Please include the text from the sample - the font needs to be the same style as what we are using on the left side!

The graphic needs to be a .png file, roughly 713 x 527 white background. Use discretion on design layout.

Colors are black, Red = PMS 1795 and Gray = Cool Gray 10

Thanks,
Tom Farrow

Target Market(s)

small businesses

Industry/Entity Type

Information Technology

Font styles to use
Other font styles liked:
• See sample

Requirements
Must have
• see description
Nice to have
• Possibly small technology related image to help enhance the text but I don't want any image to compete with the text. Keep in mind the colors mentioned in the description - this is the web site colors.
Should not have
• Should not be hard to read

```html
<!DOCTYPE html>
<html lang="en">
<head>
<meta charset="utf-8">
<title>Free Network &amp; Computer Health Check</title>
<link rel="stylesheet" href="https://fonts.googleapis.com/css2?family=Oswald:wght@300;400;500&display=swap">
<style>
  :root {
    --matte: #9a9a9a;
    --paper: #fafafa;
    --brand-red: #de3131;
    --cool-gray: #5d5c5b;
    --ink: #626366;
    --white: #ffffff;
  }
  * { box-sizing: border-box; margin: 0; padding: 0; }
  html, body {
    width: 1200px; height: 838px; overflow: hidden;
    background: var(--matte);
    font-family: "Oswald", sans-serif;
  }
  .canvas { position: relative; width: 1200px; height: 838px; }
  .card {
    position: absolute; left: 244px; top: 166px;
    width: 711px; height: 505px;
    background: var(--paper);
    overflow: hidden;
  }
  .nav-clip {
    position: absolute; left: 0; top: 0; width: 698px; height: 120px;
    overflow: hidden;
  }
  .main-nav {
    position: absolute; left: 17px; top: 33px;
    width: 700px; height: 65px;
    background: var(--brand-red);
    border-radius: 4px 0 0 4px;
    box-shadow: 0 6px 8px rgba(0,0,0,0.18);
  }
  .nav-item {
    position: absolute; top: 0; height: 65px; line-height: 65px;
    color: var(--white); font-size: 18.5px; font-weight: 500;
    letter-spacing: 0.2px; text-transform: uppercase; white-space: nowrap;
  }
  .nav-item.is-active { background: var(--cool-gray); text-align: center; }
  .nav-caret { display: inline-block; margin-left: 6px; vertical-align: middle; }
  .headline {
    position: absolute; left: 44px; top: 191px; transform: translateY(-100%);
    color: var(--ink); font-size: 35px; font-weight: 400;
    letter-spacing: -0.3px; white-space: nowrap; line-height: 1;
  }
  .checklist { position: absolute; left: 44px; top: 227px; list-style: none; }
  .checklist li {
    position: relative; height: 28px; line-height: 28px;
    padding-left: 24px; color: var(--ink);
    font-size: 14.5px; font-weight: 300; white-space: nowrap;
  }
  .checklist svg { position: absolute; left: 0; top: 5px; }
  .cta {
    position: absolute; left: 43px; top: 412px;
    width: 216px; height: 44px;
    border: 1.5px solid var(--brand-red); border-radius: 22px;
    background: var(--paper);
    box-shadow: 0 10px 10px -4px rgba(0,0,0,0.22);
    color: var(--ink); font-size: 15px; font-weight: 400;
    letter-spacing: -0.3px; text-align: center; line-height: 41px;
  }
  .pointer { position: absolute; left: 134px; top: 32px; }
</style>
</head>
<body>
<div class="canvas">
  <section class="card">
    <div class="nav-clip">
      <nav class="main-nav">
        <span class="nav-item is-active" style="left:82px;width:95px;">Home</span>
        <span class="nav-item" style="left:200px;">About</span>
        <span class="nav-item" style="left:302px;">Team</span>
        <span class="nav-item" style="left:393px;">What makes us different<svg class="nav-caret" width="8" height="6" viewBox="0 0 8 6"><path d="M1 1.5 L4 4.5 L7 1.5" fill="none" stroke="#fff" stroke-width="1.6"/></svg></span>
        <span class="nav-item" style="left:659px;">Services</span>
      </nav>
    </div>

    <h1 class="headline">FREE Network &amp; Computer health check Service</h1>

    <ul class="checklist">
      <li><svg width="16" height="15" viewBox="0 0 16 15"><rect x="0.7" y="3" width="11" height="11" fill="none" stroke="#626366" stroke-width="1.2"/><path d="M3 8 L6 11 L14.5 0.8" fill="none" stroke="#de3131" stroke-width="1.6"/></svg>Check your network's security against hacker attacks, theft, ransomware, viruses, and more.</li>
      <li><svg width="16" height="15" viewBox="0 0 16 15"><rect x="0.7" y="3" width="11" height="11" fill="none" stroke="#626366" stroke-width="1.2"/><path d="M3 8 L6 11 L14.5 0.8" fill="none" stroke="#de3131" stroke-width="1.6"/></svg>See who and what has access to your network and data.</li>
      <li><svg width="16" height="15" viewBox="0 0 16 15"><rect x="0.7" y="3" width="11" height="11" fill="none" stroke="#626366" stroke-width="1.2"/><path d="M3 8 L6 11 L14.5 0.8" fill="none" stroke="#de3131" stroke-width="1.6"/></svg>Perform network and Internet speed test</li>
      <li><svg width="16" height="15" viewBox="0 0 16 15"><rect x="0.7" y="3" width="11" height="11" fill="none" stroke="#626366" stroke-width="1.2"/><path d="M3 8 L6 11 L14.5 0.8" fill="none" stroke="#de3131" stroke-width="1.6"/></svg>Resolve PC slowness issues, security vulnerabilities and improper configurations</li>
      <li><svg width="16" height="15" viewBox="0 0 16 15"><rect x="0.7" y="3" width="11" height="11" fill="none" stroke="#626366" stroke-width="1.2"/><path d="M3 8 L6 11 L14.5 0.8" fill="none" stroke="#de3131" stroke-width="1.6"/></svg>Validate your backups are working and recoverable in a timely fashion.</li>
    </ul>

    <div class="cta">BOOK AN APPOINTMENT NOW!
      <svg class="pointer" width="22" height="26" viewBox="0 0 22 26">
        <path d="M5 2 a1.6 1.6 0 0 1 3.2 0 V11 M8.2 9 a1.6 1.6 0 0 1 3.2 0 V11.5 M11.4 10 a1.6 1.6 0 0 1 3.2 0 V12 M14.6 11 a1.6 1.6 0 0 1 3.2 0 V17 C17.8 21 15.5 24 12 24 H10 C7.5 24 6 22.5 4.5 20 L1.4 14.2 a1.5 1.5 0 0 1 2.6 -1.5 L5 14.5 V2"
              fill="#fff" stroke="#333" stroke-width="1" stroke-linejoin="round"/>
      </svg>
    </div>
  </section>
</div>
</body>
</html>
```